A Fielding Venture Book Cover Design

I require a book cover design to be completed for my book "A Fielding Venture" How to build a highly profitable sports store!

This is my third attempt at engaging a graphic designer for this project. My last attempt was a terrible experience and ended up costing me more than double my original budget.

The successful designer will be engaged for more monthly jobs as they come to hand which would be brochure designs, web graphics etc.

I'm initially looking for this cover to drive online engagement, and sell this manuscript on Quillpad with the vision to later roll out a hard copy in 6-12 months time.

My business is called The Counter Mate - I'm a retail expert consultant who specialises in advanced shop floor retail solutions. I've worked with some of Australia's largest sporting goods retailers and have trained over 5000 employees. My goal is to inspire retail standards to greater levels, and continue helping to this industry employ millions of people around the world. I'm known for inspiring my clients to pivot their retail approach to more sustainable and long term strategies.

Please find attached a design brief.

Any questions, please ask upfront.
Updates

*important* all designers read the design brief thoroughly.

```html
<!DOCTYPE html>
<html lang="en">
<head>
<meta charset="utf-8">
<title>A Fielding Venture — Book Cover</title>
<link href="https://fonts.googleapis.com/css2?family=Anton&family=Archivo+Narrow:wght@700&display=swap" rel="stylesheet">
<style>
  :root {
    --cover-grey: #a7a7a7;
    --sign-pink: #e000a2;
    --sign-rim: #ffffff;
    --facade: #666666;
    --doorway: #545454;
    --crack-dark: #2a2a2a;
    --crack-mid: #8a8a8a;
    --title-white: #ffffff;
    --ink: #111111;
  }
  html, body {
    margin: 0;
    padding: 0;
    width: 927px;
    height: 1200px;
    overflow: hidden;
    background: var(--cover-grey);
  }
  .cover {
    position: relative;
    width: 927px;
    height: 1200px;
    background: var(--cover-grey);
    overflow: hidden;
  }
  .cover-art {
    position: absolute;
    inset: 0;
  }
  .sign-board { fill: var(--sign-pink); stroke: var(--sign-rim); stroke-width: 9; }
  .facade { fill: var(--facade); }
  .doorway { fill: var(--doorway); }
  .title-line,
  .author-name {
    font-family: "Anton", "Impact", sans-serif;
    fill: var(--title-white);
    stroke: #d9d9d9;
    stroke-width: 1;
  }
  .tagline {
    position: absolute;
    left: 90px;
    top: 912px;
    margin: 0;
    font-family: "Archivo Narrow", "Arial Narrow", sans-serif;
    font-weight: 700;
    font-size: 33px;
    line-height: 41px;
    color: var(--ink);
  }
</style>
</head>
<body>
<main class="cover">
  <svg class="cover-art" width="927" height="1200" viewBox="0 0 927 1200" xmlns="http://www.w3.org/2000/svg">
    <defs>
      <filter id="raised-letter" x="-10%" y="-10%" width="130%" height="140%">
        <feDropShadow dx="5" dy="6" stdDeviation="3" flood-color="#000" flood-opacity="0.75"/>
      </filter>
      <linearGradient id="spill-tones" x1="0" y1="0" x2="1" y2="1">
        <stop offset="0" stop-color="var(--crack-dark)"/>
        <stop offset="0.45" stop-color="#555"/>
        <stop offset="1" stop-color="var(--crack-mid)"/>
      </linearGradient>
    </defs>

    <!-- Storefront sign -->
    <path class="sign-board" d="M57,420 L57,200 L72,200 L72,178 Q460,40 848,178 L848,430 Z"/>

    <!-- Shop facade and doorway -->
    <rect class="facade" x="0" y="410" width="400" height="470"/>
    <rect class="doorway" x="344" y="706" width="110" height="174"/>

    <!-- Cracked wall with spilling sports balls -->
    <polygon role="img" aria-label="Illustration of a crack splitting the shop wall with soccer balls, footballs, bowling balls and hockey pucks pouring out"
      fill="url(#spill-tones)"
      points="848,160 880,185 927,300 927,1200 640,1200 560,1100 470,960 395,870 430,760 520,640 640,470 740,300"/>

    <!-- Title -->
    <g filter="url(#raised-letter)">
      <text class="title-line" x="463" y="220" text-anchor="middle" font-size="140">A</text>
      <text class="title-line" x="118" y="400" font-size="200" textLength="748" lengthAdjust="spacingAndGlyphs">FIELDING</text>
      <text class="title-line" x="86" y="653" font-size="255" textLength="755" lengthAdjust="spacingAndGlyphs">VENTURE</text>
      <text class="author-name" x="87" y="1119" font-size="93" textLength="760" lengthAdjust="spacingAndGlyphs">DECLAN HOLLOWAY</text>
    </g>
  </svg>

  <p class="tagline">PROFIT MORE for your<br>SPORTS STORE!</p>
</main>
</body>
</html>
```